A modern, fresh introduction to Buddhism

I need a book cover for an A6 sized book to be used both for ebook and hard copy. The author is a young, modern Buddhist teacher of high standing who has written this short intro to Buddhism in an informal Q & As format using modern, accessible language to convey profound and meaningful ideas to the general public. The author is Tibetan, but teaches worldwide and is very personable and dynamic. The cover should portray this and have a fresh yet authentic feel to it (nothing new-agey!). Please see the author's websites www.torvanelmiro.org and www.wbrt.org for reference, but do not feel that the design must align completely with the website designs.

Target Market(s)

General public both in Europe and America and in Asia ranging from teenagers to the elderly. A really broad audience.

Industry/Entity Type

Teacher

Requirements
Must have
• Please include the following text that on the front cover:

A Breath of Quiet Rivers

By Venerable Tsomar Deleng

Please include the following on the back cover:

Yarkun Tselpa Publications (with attached logo above it)
Nice to have
• A simplistic, artistic, and modern look without any traditional religious images.
Should not have
• No buddha images or religious images. I would prefer a more simplistic, modern and artistic look.

```html
<!DOCTYPE html>
<html lang="en">
<head>
<meta charset="utf-8">
<title>A Breath of Quiet Rivers — Book Cover</title>
<link href="https://fonts.googleapis.com/css2?family=Oswald:wght@300;400&display=swap" rel="stylesheet">
<style>
  :root {
    --backdrop: #3f7f86;
    --paper: #ffffff;
    --title: #ffffff;
    --imprint: #3a3a3a;
  }
  * { margin: 0; padding: 0; box-sizing: border-box; }
  html, body {
    width: 1200px;
    height: 900px;
    overflow: hidden;
    background: var(--backdrop);
  }
  .cover {
    position: absolute;
    left: 65px;
    top: 62px;
    width: 1070px;
    height: 752px;
    background: var(--paper);
    overflow: hidden;
    font-family: "Oswald", "Arial Narrow", sans-serif;
  }
  .ink-cloud {
    position: absolute;
    inset: 0;
    background:
      radial-gradient(ellipse 170px 260px at 700px 230px, rgba(180,20,42,0.95), rgba(180,20,42,0) 100%),
      radial-gradient(ellipse 170px 220px at 900px 300px, rgba(180,20,42,0.9), rgba(180,20,42,0) 100%),
      radial-gradient(ellipse 120px 90px at 560px 80px, rgba(180,20,42,0.85), rgba(180,20,42,0) 100%),
      radial-gradient(ellipse 70px 60px at 300px 160px, rgba(207,43,90,0.7), rgba(207,43,90,0) 100%),
      radial-gradient(ellipse 220px 280px at 760px 430px, rgba(217,162,15,0.9), rgba(217,162,15,0) 100%),
      radial-gradient(ellipse 300px 340px at 830px 620px, rgba(227,210,26,0.95), rgba(227,210,26,0) 100%),
      radial-gradient(ellipse 260px 150px at 450px 170px, rgba(227,210,26,0.85), rgba(227,210,26,0) 100%),
      radial-gradient(ellipse 200px 80px at 120px 40px, rgba(227,210,26,0.8), rgba(227,210,26,0) 100%),
      radial-gradient(ellipse 130px 90px at 1020px 60px, rgba(227,210,26,0.8), rgba(227,210,26,0) 100%),
      radial-gradient(ellipse 180px 260px at 560px 560px, rgba(227,210,26,0.7), rgba(227,210,26,0) 100%);
  }
  .title-block {
    position: absolute;
    left: 585px;
    top: 168px;
    width: 430px;
    color: var(--title);
  }
  .title-lead {
    display: block;
    font-weight: 300;
    font-size: 58px;
    line-height: 1;
    text-transform: uppercase;
    letter-spacing: 0.5px;
  }
  .title-main {
    display: block;
    font-weight: 300;
    font-size: 100px;
    line-height: 1.08;
    margin-top: 8px;
    letter-spacing: -1.5px;
    white-space: nowrap;
  }
  .byline {
    margin-top: 14px;
    font-weight: 400;
  }
  .byline-by {
    display: block;
    font-size: 24px;
    line-height: 1.2;
    text-transform: uppercase;
  }
  .byline-author {
    display: block;
    font-size: 28px;
    line-height: 1.3;
  }
  .imprint {
    position: absolute;
    left: 62px;
    top: 490px;
    width: 120px;
    text-align: center;
    color: var(--imprint);
    font-weight: 400;
    text-transform: uppercase;
  }
  .imprint-mark {
    display: block;
    width: 64px;
    height: 64px;
    margin: 0 auto 22px;
    border-radius: 50%;
    background: var(--imprint);
  }
  .imprint-name {
    font-size: 21px;
    line-height: 1.05;
    letter-spacing: 1px;
  }
  .imprint-sub {
    font-size: 11px;
    letter-spacing: 1.5px;
    margin-top: 4px;
  }
</style>
</head>
<body>
  <main class="cover">
    <div class="ink-cloud" role="img" aria-label="Swirling clouds of yellow and crimson ink dispersing in water"></div>

    <section class="title-block">
      <h1>
        <span class="title-lead">A Breath of</span>
        <span class="title-main">Quiet Rivers</span>
      </h1>
      <p class="byline">
        <span class="byline-by">By</span>
        <span class="byline-author">Venerable Tsomar Deleng</span>
      </p>
    </section>

    <footer class="imprint">
      <span class="imprint-mark" aria-hidden="true"></span>
      <p class="imprint-name">Yarkun<br>Tselpa</p>
      <p class="imprint-sub">Publications</p>
    </footer>
  </main>
</body>
</html>
```